Hydrographic business needs a business card that reaches hunters and off-road enthusiasts

We need a business card for a new hydrographics company catering to customers such as hunters, off-road ATV riders and custom vehicle enthusiasts. A western theme is preferred but professional. Our service should be thought of as upper end graphic design on firearms, off road vehicles, motorcycles, etc... See www.ridgebackhg.com for ideas on patterns, colors, etc...

Target Market(s)

Hunters, off road enthusiasts, custom car enthusiasts, motorcycle riders...

Industry/Entity Type

Graphic Design

```html
<!DOCTYPE html>
<html lang="en">
<head>
<meta charset="utf-8">
<title>Ridgeback Hydro Graphics – Business Card</title>
<link rel="stylesheet" href="https://fonts.googleapis.com/css2?family=Open+Sans:wght@400;600;700&family=Michroma&display=swap">
<style>
  :root {
    --page: #f4f4f4;
    --wood-dark: #4a3526;
    --wood-mid: #6e5340;
    --wood-light: #8a6d57;
    --band-red: #8e1b1f;
    --band-red-dark: #6d1216;
    --band-line: #e9d6d6;
    --text-light: #ffffff;
    --service-gold: #f1c9a6;
    --mark-silver: #d8d8d8;
  }
  * { box-sizing: border-box; margin: 0; padding: 0; }
  html, body { width: 1200px; height: 900px; overflow: hidden; }
  body {
    background: var(--page);
    font-family: "Open Sans", Arial, sans-serif;
    position: relative;
  }
  .card {
    position: absolute;
    top: 295px;
    width: 540px;
    height: 310px;
    border-radius: 22px;
    overflow: hidden;
    box-shadow: 0 10px 24px rgba(0,0,0,0.22);
  }
  .card--front { left: 40px; }
  .card--back { left: 620px; }
  .wood {
    position: absolute;
    inset: 0;
    background: linear-gradient(100deg, var(--wood-dark) 0%, var(--wood-mid) 35%, var(--wood-light) 55%, var(--wood-mid) 80%, var(--wood-dark) 100%);
  }
  /* front */
  .brand-mark {
    position: absolute;
    left: 130px;
    top: 72px;
    display: flex;
    align-items: center;
    gap: 16px;
  }
  .brand-mark__dot {
    width: 56px; height: 56px;
    border-radius: 50%;
    background: var(--mark-silver);
    flex: none;
  }
  .brand-mark__name {
    color: var(--mark-silver);
    font-weight: 700;
    font-size: 28px;
    line-height: 1.15;
    letter-spacing: 1px;
    text-transform: uppercase;
  }
  .tagline-band {
    position: absolute;
    left: 0; right: 0;
    top: 248px;
    height: 24px;
    background: var(--band-red);
    border-top: 1.5px solid var(--band-line);
    border-bottom: 1.5px solid var(--band-line);
    display: flex;
    align-items: center;
    justify-content: center;
    padding: 0 18px;
  }
  .tagline {
    font-family: "Michroma", Arial, sans-serif;
    font-size: 7.6px;
    letter-spacing: 0.9px;
    color: var(--text-light);
    text-transform: uppercase;
    white-space: nowrap;
  }
  /* back */
  .holder-name {
    position: absolute;
    left: 28px; top: 26px;
    color: var(--text-light);
    font-weight: 700;
    font-size: 24px;
    letter-spacing: 0.5px;
    text-transform: uppercase;
  }
  .faint-name {
    position: absolute;
    left: 170px; top: 80px;
    width: 260px;
    color: rgba(255,255,255,0.12);
    font-weight: 700;
    font-size: 28px;
    line-height: 1.1;
    text-transform: uppercase;
    text-align: center;
  }
  .contact-band {
    position: absolute;
    left: 0; right: 0;
    top: 180px;
    height: 110px;
    background: linear-gradient(180deg, var(--band-red) 0%, var(--band-red-dark) 100%);
    border-top: 1.5px solid var(--band-line);
    border-bottom: 1.5px solid var(--band-line);
    padding: 10px 18px 0 20px;
    display: flex;
    justify-content: space-between;
  }
  .contact-list { list-style: none; }
  .contact-list li {
    display: flex;
    align-items: center;
    gap: 8px;
    color: var(--text-light);
    font-size: 15px;
    line-height: 18px;
  }
  .contact-list .icon { width: 16px; height: 16px; flex: none; }
  .contact-list .indent { padding-left: 24px; }
  .service-list { list-style: none; padding-top: 2px; }
  .service-list li {
    color: var(--service-gold);
    font-weight: 600;
    font-size: 12.5px;
    margin-bottom: 18px;
  }
</style>
</head>
<body>

<section class="card card--front" aria-label="Card front">
  <div class="wood" role="img" aria-label="Weathered vertical wooden plank background"></div>
  <div class="brand-mark">
    <span class="brand-mark__dot"></span>
    <span class="brand-mark__name">Ridgeback<br>Hydro Graphics</span>
  </div>
  <div class="tagline-band">
    <p class="tagline">The best and most reliable hydrographics service in Texas</p>
  </div>
</section>

<section class="card card--back" aria-label="Card back">
  <div class="wood" role="img" aria-label="Weathered vertical wooden plank background"></div>
  <h1 class="holder-name">Cody Harlan</h1>
  <p class="faint-name" aria-hidden="true">Ridgeback<br>Hydro</p>
  <div class="contact-band">
    <ul class="contact-list">
      <li>
        <svg class="icon" viewBox="0 0 16 16" fill="none" stroke="#fff" stroke-width="1.4"><path d="M3 2l3 0 1 3-2 1.5a8 8 0 0 0 4.5 4.5L11 9l3 1v3a1.5 1.5 0 0 1-1.5 1.5A11 11 0 0 1 1.5 3.5 1.5 1.5 0 0 1 3 2z"/></svg>
        214-555-0187
      </li>
      <li>
        <svg class="icon" viewBox="0 0 16 16" fill="none" stroke="#fff" stroke-width="1.4"><path d="M1.5 8L8 2l6.5 6M3.5 6.5V14h3.5v-4h2v4h3.5V6.5"/></svg>
        612 County Road 2140
      </li>
      <li class="indent">Cedar Flats, TX 75000</li>
      <li>
        <svg class="icon" viewBox="0 0 16 16" fill="none" stroke="#fff" stroke-width="1.2"><circle cx="8" cy="8" r="6.5"/><ellipse cx="8" cy="8" rx="3" ry="6.5"/><path d="M1.5 8h13M2.5 5h11M2.5 11h11"/></svg>
        www.ridgebackhg.com
      </li>
      <li>
        <svg class="icon" viewBox="0 0 16 16" fill="none" stroke="#fff" stroke-width="1.3"><rect x="1.5" y="3.5" width="13" height="9" rx="1"/><path d="M1.5 4l6.5 5 6.5-5"/></svg>
        cody@ridgebackhg.com
      </li>
    </ul>
    <ul class="service-list">
      <li>Firearm Hydrographics</li>
      <li>ATV Hydrographics</li>
      <li>Hydrographics</li>
    </ul>
  </div>
</section>

</body>
</html>
```